Fontenot Bayou Grillhouse (Owners Card)

Need a classy, but modern business card. I have included a promotional card for the steakhouse. I need one for myself (the owner) that is more professional.

Target Market(s)

General Public

Industry/Entity Type

Food service

Contact Information for Business Card

Name, business address, phone number, email, logo

Font styles to use
Serif
Sans Serif
Decorative
Script

Requirements
Must have
• My name (Darvel Pruitt), business address (327 Oakmere Street), phone number (510) 493-2615, email (Dpruittkr4@mailvane.example. On the back of the card: Psalms 27 1 The LORD is my light and my salvation— whom shall I fear? The LORD is the stronghold of my life— of whom shall I be afraid? 2 When the wicked advance against me to devour me, it is my enemies and my foes who will stumble and fall. 3 Though an army besiege me, my heart will not fear; though war break out against me, even then I will be confident.
Nice to have
• Something that’s bold, but modern and professional.

```html
<!DOCTYPE html>
<html lang="en">
<head>
<meta charset="utf-8">
<title>Fontenot Bayou Grillhouse – Owner Card</title>
<link href="https://fonts.googleapis.com/css2?family=Cinzel:wght@700&family=Roboto:wght@400&display=swap" rel="stylesheet">
<style>
  :root {
    --backdrop: #3b3b3d;
    --card: #1c1c1d;
    --green: #3dbb4a;
    --lime: #b9d532;
    --yellow: #f6b41c;
    --orange: #f47c20;
    --red: #e8202a;
    --white: #f4f4f4;
    --brand: #f39a1e;
  }
  * { box-sizing: border-box; margin: 0; padding: 0; }
  html, body { width: 1200px; height: 895px; overflow: hidden; background: var(--backdrop); }
  .canvas { position: relative; width: 1200px; height: 895px; }
  .card {
    position: absolute; left: 290px; width: 620px; height: 354px;
    background: var(--card); border-radius: 18px; overflow: hidden;
    box-shadow: 0 10px 30px rgba(0,0,0,.45);
  }
  .card--back { top: 60px; }
  .card--front { top: 474px; }
  .accent-stripe {
    position: absolute; left: 0; right: 0; bottom: 0; height: 9px;
    background: linear-gradient(90deg, var(--green), var(--lime) 30%, var(--yellow) 55%, var(--orange) 78%, var(--red));
  }
  .brand {
    position: absolute; left: 0; right: 0; top: 50%; transform: translateY(-50%);
    display: flex; flex-direction: column; align-items: center; gap: 14px;
  }
  .brand__dot { width: 46px; height: 46px; border-radius: 50%; background: var(--brand); }
  .brand__name {
    font-family: "Cinzel", serif; font-weight: 700; font-size: 30px;
    color: var(--brand); letter-spacing: 1px; text-align: center; line-height: 1.15;
  }
  .identity { position: absolute; left: 36px; top: 150px; width: 205px; }
  .identity__name {
    font-family: "Cinzel", serif; font-weight: 700; font-size: 21px; letter-spacing: .5px;
    white-space: nowrap;
    background: linear-gradient(90deg, var(--green), var(--yellow) 45%, var(--orange) 70%, var(--red));
    -webkit-background-clip: text; background-clip: text; color: transparent;
  }
  .identity__role { font-family: "Roboto", sans-serif; font-size: 16px; color: var(--white); margin-top: 4px; }
  .mark {
    position: absolute; left: 248px; top: 100px; width: 120px;
    display: flex; flex-direction: column; align-items: center; gap: 10px;
  }
  .mark__disc { width: 104px; height: 104px; border-radius: 50%; background: var(--brand); }
  .mark__name {
    font-family: "Cinzel", serif; font-weight: 700; font-size: 11px; line-height: 1.3;
    color: var(--brand); text-align: center;
  }
  .contact { position: absolute; right: 24px; top: 130px; list-style: none; }
  .contact__item {
    display: flex; justify-content: flex-end; align-items: center; gap: 8px;
    font-family: "Roboto", sans-serif; font-size: 14px; color: var(--white); line-height: 24px;
    white-space: nowrap;
  }
  .contact__item svg { width: 14px; height: 14px; flex: none; }
</style>
</head>
<body>
<main class="canvas">
  <section class="card card--back" aria-label="Card back">
    <div class="brand">
      <span class="brand__dot"></span>
      <span class="brand__name">Fontenot Bayou<br>Grillhouse</span>
    </div>
    <div class="accent-stripe"></div>
  </section>

  <section class="card card--front" aria-label="Card front">
    <div class="identity">
      <p class="identity__name">DARVEL PRUITT</p>
      <p class="identity__role">Owner/CEO</p>
    </div>
    <div class="mark">
      <span class="mark__disc"></span>
      <span class="mark__name">Fontenot Bayou<br>Grillhouse</span>
    </div>
    <ul class="contact">
      <li class="contact__item">327 Oakmere Street
        <svg viewBox="0 0 16 16"><path d="M8 1a5 5 0 0 0-5 5c0 4 5 9 5 9s5-5 5-9a5 5 0 0 0-5-5z" fill="var(--red)"/><circle cx="8" cy="6" r="2" fill="var(--card)"/></svg>
      </li>
      <li class="contact__item">(510) 493-2615
        <svg viewBox="0 0 16 16"><path d="M4 1.5l2.5 3-1.5 1.5c.8 2 2.5 3.7 4.5 4.5l1.5-1.5 3 2.5-1.5 2.5C7 14 2 9 1.5 3z" fill="var(--green)"/></svg>
      </li>
      <li class="contact__item">Dpruittkr4@mailvane.example
        <svg viewBox="0 0 16 16"><rect x="1" y="3" width="14" height="10" rx="1" fill="var(--red)"/><path d="M1.5 3.5L8 9l6.5-5.5" stroke="var(--card)" stroke-width="1.3" fill="none"/></svg>
      </li>
      <li class="contact__item">www.fontenotbayou.example
        <svg viewBox="0 0 16 16" fill="none" stroke="var(--green)" stroke-width="1.4"><circle cx="8" cy="8" r="6.3"/><ellipse cx="8" cy="8" rx="2.8" ry="6.3"/><path d="M1.7 8h12.6M3 4.5h10M3 11.5h10"/></svg>
      </li>
    </ul>
  </section>
</main>
</body>
</html>
```